Landing page design for secure cloud backup web application

We would like a landing page design for our web application. Our app allows users to securely save their data in the cloud using their existing storage providers, such as tidLoft, Keg, Velmora Sky Locker, Pintaro stash and Quelvix Sole vault.
We make it extremely easy for individual users and small businesses to deploy sophisticated client-side encryption without having to worry about the technical complexity inherent in such solutions.
We already have the logo design done - I am attaching the logo file. We also have a preliminary website drafted at www.pemraq.test
I need a good color scheme, typography, layout, along with templates for 'help', 'about', 'privacy notice', 'legal' and such typical sub-pages
The design should be uncluttered, clean and minimalist

Target Market(s)

Individuals and medium/small businesses that are conscious about the security of their data in the cloud

Coding

Coded - Design and coding required

Number of Pages Required

4 page

Font styles to use
Sans Serif

Requirements
Must have
• Section where I describe the product along with pictures/images
• section for explainer video on main page
• FAQ section
• Help section
• Legal/privacynotice/terms of use section
• feedback section
Nice to have
• see existing draft site www.pemraq.test for content guidelines only.
• see attached logo files for color scheme guidelines - I am willing to accept change in the logo color if necessary to create a better web site look and feel
• Fonts on page should match font in the logo

```html
<!DOCTYPE html>
<html lang="en">
<head>
<meta charset="utf-8">
<title>Pemraq – Keep your data private</title>
<link rel="stylesheet" href="https://fonts.googleapis.com/css2?family=Poppins:wght@300;400;600&display=swap">
<style>
  :root {
    --orange: #e5972d;
    --orange-deep: #da8b24;
    --white: #ffffff;
    --band: #f4f4f4;
    --art-dark: #262626;
    --art-mid: #4a4a4a;
    --art-silver: #c4c5c8;
  }
  * { box-sizing: border-box; margin: 0; padding: 0; }
  html, body { width: 1200px; height: 1000px; overflow: hidden; }
  body {
    font-family: "Poppins", sans-serif;
    background: var(--band);
    color: var(--white);
    position: relative;
  }
  .hero {
    position: absolute; left: 0; top: 0; width: 1200px; height: 870px;
    background: linear-gradient(180deg, var(--orange) 0%, var(--orange-deep) 100%);
  }
  .hero-art {
    position: absolute; left: 270px; top: 0; width: 660px; height: 340px;
    background: linear-gradient(180deg, var(--art-dark) 0%, var(--art-mid) 72%, var(--art-silver) 100%);
  }
  .hero-title {
    position: absolute; top: 384px; left: 0; width: 100%;
    text-align: center; font-weight: 400; font-size: 29px; line-height: 1.3;
  }
  .feature-icon {
    position: absolute; width: 104px; height: 104px; border-radius: 50%;
    border: 2px solid var(--white);
    display: flex; align-items: center; justify-content: center;
  }
  .feature-icon svg { width: 48px; height: 48px; fill: none; stroke: var(--white); stroke-width: 2.4; stroke-linecap: round; stroke-linejoin: round; }
  .feature-icon--active { background: var(--white); width: 120px; height: 120px; border: none; }
  .feature-icon--active svg { stroke: var(--orange); width: 56px; height: 56px; }
  .connector {
    position: absolute; left: 284px; top: 600px; width: 190px; height: 110px;
    border-left: 3px dotted var(--white); border-bottom: 3px dotted var(--white);
  }
  .feature-detail { position: absolute; top: 630px; left: 490px; width: 440px; text-align: center; }
  .feature-detail h2 { font-weight: 600; font-size: 20px; letter-spacing: 0.5px; margin-bottom: 14px; }
  .feature-detail p { font-weight: 300; font-size: 14px; line-height: 1.5; }
</style>
</head>
<body>
  <section class="hero">
    <div class="hero-art" role="img" aria-label="Product illustration: open laptop with a dark screen"></div>
    <h1 class="hero-title">Keep your data private without breaking a sweat</h1>

    <div class="feature-icon feature-icon--active" style="left:224px;top:480px" aria-label="Partnership">
      <svg viewBox="0 0 50 50"><path d="M3 20l8-6 8 4 6-3 6 3 8-4 8 6"/><path d="M11 14l-6 14 10 8"/><path d="M39 14l6 14-10 8"/><path d="M19 18l-5 5 3 3 8-6 10 10-3 3-4-4 2 6-3 2-3-4 1 4-3 2-4-4"/></svg>
    </div>
    <div class="feature-icon" style="left:392px;top:476px" aria-label="Secure safe">
      <svg viewBox="0 0 50 50"><rect x="8" y="6" width="34" height="34" rx="3"/><circle cx="24" cy="23" r="7"/><path d="M36 16v14M12 40v4M38 40v4"/></svg>
    </div>
    <div class="feature-icon" style="left:548px;top:464px" aria-label="Cloud on screen">
      <svg viewBox="0 0 50 50"><rect x="5" y="8" width="40" height="28" rx="2"/><path d="M25 36v6M17 42h16"/><path d="M18 28h14a4 4 0 0 0 0-8 6 6 0 0 0-11-2 4 4 0 0 0-3 10z"/><path d="M25 21v6M23 23l2-2 2 2"/></svg>
    </div>
    <div class="feature-icon" style="left:704px;top:452px" aria-label="Global location">
      <svg viewBox="0 0 50 50"><circle cx="23" cy="27" r="17"/><path d="M10 22c5 0 6 4 10 4s3 6 0 9M28 12c-2 4 2 6 5 6M30 42c0-5 4-6 7-8"/><path d="M36 20c-4-5-7-8-7-12a7 7 0 0 1 14 0c0 4-3 7-7 12z"/><circle cx="36" cy="8" r="2"/></svg>
    </div>
    <div class="feature-icon" style="left:852px;top:438px" aria-label="Documents">
      <svg viewBox="0 0 50 50"><path d="M14 10h20v30H14z"/><path d="M10 14v30h20"/><path d="M18 6h20v30"/></svg>
    </div>

    <div class="connector" aria-hidden="true"></div>

    <div class="feature-detail">
      <h2>USE YOUR CLOUD</h2>
      <p>Pemraq lets you use the accounts you already have and trust, such as Keg, tidLoft, Velmora Sky Locker, Quelvix Sole vault and Pintaro stash without breaking a sweat</p>
    </div>
  </section>
</body>
</html>
```